Web design required

1-We need a web design for existing company based in New Zealand
2-We build residential house and light commercial
3-We has in-house designer which allow us can provide interior design
4-We modeling project before site construction, which enable both client and construction team to visually analysis whole project,

Target Market(s)

middle class residential house market
Ref: http://www.brambleworthbuilders.co.nz/

Industry/Entity Type

Construction Company

Number of Pages Required

1 page

Font styles to use
Sans Serif
Other font styles liked:
• Such as : Central Gothic or similar which has more design taste

Colors

Designer to choose colors to be used in the design.

Requirements
Must have
• Front sheet, contact information, sample project

```html
<!DOCTYPE html>
<html lang="en">
<head>
<meta charset="utf-8">
<title>Kestrel Homes</title>
<link rel="stylesheet" href="https://fonts.googleapis.com/css2?family=Lato:wght@300;400;700;900&family=Open+Sans:wght@400;600;700&display=swap">
<style>
:root{
  --blue:#1565a8;
  --blue-dark:#0f4f86;
  --navy:#0e2a48;
  --ink:#2a2a2a;
  --text:#555;
  --muted:#888;
  --light:#f4f4f4;
  --line:#e2e2e2;
  --white:#fff;
  --topbar:#2b2b2b;
}
*{box-sizing:border-box;margin:0;padding:0}
html,body{width:1200px;height:4932px;overflow:hidden}
body{font-family:"Open Sans",Arial,sans-serif;color:var(--text);background:var(--white);position:relative}
.section{position:relative;width:1200px;overflow:hidden}
.abs{position:absolute}
.btn{position:absolute;display:flex;align-items:center;justify-content:center;font-family:"Lato",Arial,sans-serif;font-size:17px;letter-spacing:.5px;text-transform:uppercase}
.btn-blue{background:var(--blue);color:var(--white)}
.btn-white{background:var(--white);color:var(--blue)}
.photo{position:absolute}

/* top bar */
.topbar{height:33px;background:var(--topbar);color:#ddd;font-size:14px}
.topbar .social{left:80px;top:8px;display:flex;gap:14px}
.topbar .social span{width:16px;height:16px;border-radius:50%;background:#bbb;display:block}
.topbar .contact{right:82px;top:7px;display:flex;gap:36px;align-items:center}
.topbar .contact span{display:flex;gap:8px;align-items:center}

/* nav */
.nav{height:105px;background:var(--white)}
.brand{left:80px;top:22px;display:flex;align-items:center;gap:10px}
.brand .mark{width:40px;height:40px;border-radius:50%;background:var(--blue)}
.brand .name{font-family:"Lato",Arial,sans-serif;font-weight:700;font-size:24px;color:var(--blue);letter-spacing:3px;line-height:1}
.menu{left:440px;top:34px;display:flex;align-items:center;font-family:"Lato",Arial,sans-serif;font-size:19px;color:#666}
.menu a{text-decoration:none;color:#666;padding:0 22px;height:48px;display:flex;align-items:center}
.menu a.active{background:var(--blue);color:var(--white);padding:0 34px;margin-right:14px}

/* hero */
.hero{height:579px}
.hero .photo{inset:0;background:linear-gradient(180deg,#3a3e40 0%,#2a2c2b 45%,#3b3128 75%,#1f1f1d 100%)}
.hero .shade{position:absolute;inset:0;background:rgba(0,0,0,.35)}
.hero h1{position:absolute;left:0;width:1200px;top:160px;text-align:center;font-family:"Lato",Arial,sans-serif;font-weight:400;font-size:48px;letter-spacing:12px;color:var(--white)}
.hero h2{position:absolute;left:0;width:1200px;top:222px;text-align:center;font-family:"Lato",Arial,sans-serif;font-weight:700;font-size:33px;color:var(--white)}
.hero p{position:absolute;left:270px;width:560px;top:276px;text-align:center;font-size:14px;line-height:20px;color:#e4e4e4}

/* about */
.about{height:440px}
.about .photo{left:82px;top:56px;width:411px;height:328px;background:radial-gradient(ellipse at 50% 45%,#e6e0d6 0%,#f3f2ef 60%,#fff 100%)}
.about h2{position:absolute;left:536px;top:50px;width:560px;font-family:"Lato",Arial,sans-serif;font-weight:400;font-size:38px;line-height:37px;color:#444}
.about h2 b{color:var(--blue);font-weight:700}
.about h2 .lead{color:var(--blue)}
.about p{position:absolute;left:536px;top:176px;width:590px;font-size:14.5px;line-height:21px;color:var(--text)}

/* services */
.services{height:1036px;background:var(--light)}
.section-title{position:absolute;left:0;width:1200px;text-align:center;font-family:"Lato",Arial,sans-serif;font-weight:400;font-size:37px;color:#444}
.section-title b{color:var(--blue);font-weight:700}
.card{position:absolute;width:332px;height:369px;background:var(--white);box-shadow:0 2px 6px rgba(0,0,0,.08)}
.card .photo{left:0;top:0;width:332px;height:165px}
.card .label{position:absolute;left:10px;top:160px;width:292px;height:46px;background:var(--blue);color:var(--white);font-family:"Lato",Arial,sans-serif;font-size:20px;display:flex;align-items:center;justify-content:center}
.card p{position:absolute;left:26px;top:222px;width:280px;text-align:center;font-size:13.5px;line-height:23px;color:var(--text)}
.card .fold{position:absolute;right:0;bottom:0;width:0;height:0;border-style:solid;border-width:0 0 36px 36px;border-color:transparent transparent var(--light) #cfcfcf}

/* feedback */
.feedback{height:497px}
.feedback .photo{left:0;top:0;width:602px;height:497px;background:linear-gradient(180deg,#1c2a3c 0%,#33373a 40%,#6b4f2c 62%,#2a2520 100%)}
.feedback .panel{position:absolute;left:602px;top:0;width:598px;height:497px;background:var(--blue)}
.feedback h2{position:absolute;left:30px;top:45px;font-family:"Lato",Arial,sans-serif;font-weight:400;font-size:37px;color:var(--white)}
.feedback h2 b{font-weight:700}
.quote{position:absolute;left:28px;width:520px}
.quote .mark{position:absolute;left:0;top:0;font-family:"Lato",Arial,sans-serif;font-weight:900;font-size:44px;line-height:36px;color:var(--white)}
.quote p{position:absolute;left:50px;top:0;width:470px;font-size:13.5px;line-height:20px;color:var(--white)}
.quote .avatar{position:absolute;left:50px;top:62px;width:70px;height:70px;border-radius:50%;background:#d9dfe6;border:3px solid var(--white)}
.quote .who{position:absolute;left:140px;top:70px;color:var(--white);font-family:"Lato",Arial,sans-serif}
.quote .who strong{display:block;font-weight:400;font-size:22px}
.quote .who span{font-size:14px}

/* projects */
.projects{height:805px}
.projects .kicker{position:absolute;left:0;width:1200px;top:60px;text-align:center;font-family:"Lato",Arial,sans-serif;font-size:20px;color:#555}
.projects .rule{position:absolute;left:256px;width:688px;top:160px;height:1px;background:var(--line)}
.filters{position:absolute;left:256px;width:688px;top:172px;display:flex;justify-content:center;font-family:"Lato",Arial,sans-serif;font-size:17px;color:#666}
.filters span{padding:0 22px;border-left:1px solid #bbb;line-height:18px}
.filters span:first-child{border-left:0;color:var(--blue)}
.filters .underline{position:absolute;left:0;top:30px;width:688px;height:1px;background:var(--line)}

/* stats */
.stats{height:253px}
.stats .photo{inset:0;background:linear-gradient(90deg,#3b6d9c 0%,#4f86b5 35%,#3e74a5 70%,#2f5f8f 100%)}
.stat{position:absolute;top:52px;width:200px;text-align:center;color:var(--white)}
.stat svg{display:block;margin:0 auto 14px}
.stat strong{display:block;font-family:"Lato",Arial,sans-serif;font-size:22px;font-weight:700}
.stat span{display:block;margin-top:6px;font-family:"Lato",Arial,sans-serif;font-size:21px}

/* blog */
.blog{height:625px}
.post{position:absolute;top:152px;width:332px;height:411px;background:var(--white);box-shadow:0 2px 6px rgba(0,0,0,.08)}
.post .photo{left:0;top:0;width:332px;height:177px}
.post h3{position:absolute;left:16px;top:196px;width:300px;text-align:center;font-family:"Lato",Arial,sans-serif;font-weight:700;font-size:18px;line-height:24px;color:#333}
.post p{position:absolute;left:20px;top:256px;width:292px;text-align:center;font-size:13.5px;line-height:20px;color:var(--text)}
.post .meta{position:absolute;left:0;bottom:0;width:332px;height:50px;background:var(--blue);color:var(--white);font-size:14px;display:flex;align-items:center;padding:0 14px;gap:10px}
.post .meta span{display:flex;align-items:center;gap:7px}
.post .meta .arrow{margin-left:auto}

/* cta */
.cta{height:181px;background:var(--blue)}
.cta p{position:absolute;left:80px;top:60px;width:760px;font-family:"Lato",Arial,sans-serif;font-size:23px;line-height:32px;color:var(--white);letter-spacing:.5px;text-transform:uppercase}
.cta .btn{left:888px;top:60px;width:233px;height:64px;border:2px solid var(--white);color:var(--white);font-size:19px}

/* footer */
.footer{height:312px;background:var(--navy);color:#d6dde6;font-size:13.5px}
.footer h4{font-family:"Lato",Arial,sans-serif;font-weight:400;font-size:17px;color:var(--white);margin-bottom:16px}
.footer .col{position:absolute;top:40px}
.footer .brand-foot{left:84px;top:44px}
.footer .links li{list-style:none;line-height:28px}
.footer .contact-row{display:flex;gap:12px;margin-bottom:14px;line-height:20px}
.footer .circles{display:flex;gap:12px;margin-top:18px}
.footer .circles span{width:40px;height:40px;border-radius:50%;background:var(--blue);border:2px solid var(--white)}
.footer .email{width:250px;height:44px;background:var(--white);color:#999;font-size:13px;display:flex;align-items:center;padding:0 12px;margin-top:14px}
.footer .submit{width:110px;height:48px;background:var(--blue);color:var(--white);font-family:"Lato",Arial,sans-serif;font-size:17px;display:flex;align-items:center;justify-content:center;margin-top:14px;border:1px solid #4b8ccc}
.copyright{height:66px;background:#1b5a94;color:#dfe8f2;font-size:14px;display:flex;align-items:center;justify-content:center}
</style>
</head>
<body>

<header class="section topbar">
  <div class="abs social"><span></span><span></span><span></span><span></span></div>
  <div class="abs contact">
    <span><svg width="16" height="12" viewBox="0 0 16 12"><rect x="0.5" y="0.5" width="15" height="11" fill="none" stroke="#ddd"/><path d="M1 1l7 6 7-6" fill="none" stroke="#ddd"/></svg>info@kestrelhomes.com</span>
    <span><svg width="14" height="14" viewBox="0 0 14 14"><path d="M3 1l3 3-2 2c1 2 2 3 4 4l2-2 3 3-2 2C6 13 1 8 1 3z" fill="#ddd"/></svg>555-218-4460</span>
  </div>
</header>

<nav class="section nav">
  <div class="abs brand"><span class="mark"></span><span class="name">KESTREL<br>HOMES</span></div>
  <div class="abs menu">
    <a class="active" href="#">Home</a><a href="#">About</a><a href="#">Services</a><a href="#">Projects</a><a href="#">News</a><a href="#">Contact</a>
    <svg width="20" height="20" viewBox="0 0 20 20" style="margin-left:12px"><circle cx="8" cy="8" r="6" fill="none" stroke="#1565a8" stroke-width="2"/><path d="M12.5 12.5L18 18" stroke="#1565a8" stroke-width="2"/></svg>
  </div>
</nav>

<section class="section hero">
  <div class="photo" role="img" aria-label="Modern timber house at dusk with lit windows among trees"></div>
  <div class="shade"></div>
  <h1>KESTRELHOME</h1>
  <h2>We Build Your Dream</h2>
  <p>Lorem Ipsum is simply dummy text of the printing and typesetting industry. Lorem Ipsum has been the industry's standard dummy text ever since the 1500s.</p>
  <div class="btn btn-blue" style="left:411px;top:349px;width:171px;height:56px">Learn More</div>
  <div class="btn btn-white" style="left:605px;top:349px;width:184px;height:56px">Contact Us</div>
</section>

<section class="section about">
  <div class="photo" role="img" aria-label="Illustration of a house under construction with roof framing over plans"></div>
  <h2><span class="lead">We</span> <b>Build residential house and light commercial</b> which are terribly restless</h2>
  <p>Lorem Ipsum is simply dummy text of the printing and typesetting industry. Lorem Ipsum has been the industry's standard dummy text ever since the 1500s, when an unknown printer took a galley of type and scrambled it to make a type specimen book. It has survived not only five centuries, but also the leap into electronic typesetting, remaining essentially unchanged.</p>
  <div class="btn btn-blue" style="left:536px;top:319px;width:187px;height:59px">Learn More</div>
</section>

<section class="section services">
  <h2 class="section-title" style="top:60px">Our <b>Services</b></h2>

  <div class="card" style="left:79px;top:135px">
    <div class="photo" role="img" aria-label="Small cottage in a green garden" style="background:linear-gradient(180deg,#3f6a2c,#7a8f3a 60%,#5d4a2a)"></div>
    <div class="label">Lorem Ipsum simply dummy</div>
    <p>Lorem Ipsum is simply dummy text of the printing and typesetting industry. Lorem Ipsum has been the industry's standard dummy text ever since the 1500s.</p>
    <div class="fold"></div>
  </div>
  <div class="card" style="left:434px;top:135px">
    <div class="photo" role="img" aria-label="City skyline at night with light trails" style="background:linear-gradient(180deg,#0f1a33,#233a66 55%,#6a5a3c)"></div>
    <div class="label">Lorem Ipsum simply dummy</div>
    <p>Lorem Ipsum is simply dummy text of the printing and typesetting industry. Lorem Ipsum has been the industry's standard dummy text ever since the 1500s.</p>
    <div class="fold"></div>
  </div>
  <div class="card" style="left:789px;top:135px">
    <div class="photo" role="img" aria-label="Architect in hard hat with house model and drawings" style="background:linear-gradient(180deg,#e8e8e6,#cfd3d6 60%,#b8a98a)"></div>
    <div class="label">Lorem Ipsum simply dummy</div>
    <p>Lorem Ipsum is simply dummy text of the printing and typesetting industry. Lorem Ipsum has been the industry's standard dummy text ever since the 1500s.</p>
    <div class="fold"></div>
  </div>

  <div class="card" style="left:79px;top:572px">
    <div class="photo" role="img" aria-label="Warm interior living space with timber beams" style="background:linear-gradient(180deg,#3a2a1e,#8a6a44 55%,#4a3a2a)"></div>
    <div class="label">Lorem Ipsum simply dummy</div>
    <p>Lorem Ipsum is simply dummy text of the printing and typesetting industry. Lorem Ipsum has been the industry's standard dummy text ever since the 1500s.</p>
    <div class="fold"></div>
  </div>
  <div class="card" style="left:434px;top:572px">
    <div class="photo" role="img" aria-label="Two storey modern home at twilight" style="background:linear-gradient(180deg,#5a6b80,#8a8470 55%,#3d3a34)"></div>
    <div class="label">Lorem Ipsum simply dummy</div>
    <p>Lorem Ipsum is simply dummy text of the printing and typesetting industry. Lorem Ipsum has been the industry's standard dummy text ever since the 1500s.</p>
    <div class="fold"></div>
  </div>
  <div class="card" style="left:789px;top:572px">
    <div class="photo" role="img" aria-label="House frame under construction against the sky" style="background:linear-gradient(180deg,#9ab3c8,#c2c6c4 55%,#7a6a55)"></div>
    <div class="label">Lorem Ipsum simply dummy</div>
    <p>Lorem Ipsum is simply dummy text of the printing and typesetting industry. Lorem Ipsum has been the industry's standard dummy text ever since the 1500s.</p>
    <div class="fold"></div>
  </div>
</section>

<section class="section feedback">
  <div class="photo" role="img" aria-label="Large family home lit up at dusk"></div>
  <div class="panel">
    <h2>Our <b>Client</b> Feedback</h2>
    <div class="quote" style="top:145px">
      <span class="mark">&ldquo;</span>
      <p>Lorem Ipsum is simply dummy text of the printing and typesetting type and scrambled it to make a type specimen book.</p>
      <div class="avatar" role="img" aria-label="Client portrait"></div>
      <div class="who"><strong>mara linton</strong><span>Manager</span></div>
    </div>
    <div class="quote" style="top:305px">
      <span class="mark">&ldquo;</span>
      <p>Lorem Ipsum is simply dummy text of the printing and typesetting type and scrambled it to make a type specimen book.</p>
      <div class="avatar" role="img" aria-label="Client portrait"></div>
      <div class="who"><strong>mara linton</strong><span>Manager</span></div>
    </div>
  </div>
</section>

<section class="section projects">
  <div class="kicker">Our Projects</div>
  <h2 class="section-title" style="top:100px">Some of <b>Our Best Works</b></h2>
  <div class="rule"></div>
  <div class="filters"><span>All</span><span>Residential House</span><span>Light Commercial</span><span>New Project</span><div class="underline"></div></div>

  <div class="photo" role="img" aria-label="White weatherboard house on a lawn" style="left:79px;top:266px;width:687px;height:217px;background:linear-gradient(180deg,#8fa8bd,#c9cfd2 50%,#6b8a4a)"></div>
  <svg class="abs" style="left:394px;top:346px" width="56" height="56" viewBox="0 0 56 56"><circle cx="23" cy="23" r="15" fill="none" stroke="#fff" stroke-width="4"/><path d="M34 34l16 16" stroke="#fff" stroke-width="5"/></svg>
  <div class="photo" role="img" aria-label="Modern home with glowing windows at night" style="left:789px;top:266px;width:332px;height:217px;background:linear-gradient(180deg,#1b2538,#3a3a3a 50%,#8a5a24)"></div>
  <div class="photo" role="img" aria-label="Dark timber clad house with deck" style="left:79px;top:513px;width:332px;height:217px;background:linear-gradient(180deg,#a9b4b8,#5a5650 55%,#6b7a48)"></div>
  <div class="photo" role="img" aria-label="White villa with gabled roof" style="left:434px;top:513px;width:332px;height:217px;background:linear-gradient(180deg,#8fa6b8,#e2e2dc 55%,#4f6a38)"></div>
  <div class="photo" role="img" aria-label="Small timber cabin lit from inside" style="left:789px;top:513px;width:332px;height:217px;background:linear-gradient(180deg,#2d3d55,#a0703c 55%,#4a3a2a)"></div>
</section>

<section class="section stats">
  <div class="photo" role="img" aria-label="Interior room overlaid with blue tint"></div>
  <div class="stat" style="left:100px">
    <svg width="40" height="40" viewBox="0 0 40 40"><path d="M6 14h22v12a8 8 0 0 1-8 8h-6a8 8 0 0 1-8-8z" fill="#fff"/><path d="M28 17h4a4 4 0 0 1 0 8h-4" fill="none" stroke="#fff" stroke-width="3"/></svg>
    <strong>501</strong><span>Cup of Tea</span>
  </div>
  <div class="stat" style="left:370px">
    <svg width="40" height="40" viewBox="0 0 40 40"><path d="M20 36L5 21a9 9 0 0 1 15-11 9 9 0 0 1 15 11z" fill="#fff"/></svg>
    <strong>32,151</strong><span>Happy Clients</span>
  </div>
  <div class="stat" style="left:623px">
    <svg width="40" height="40" viewBox="0 0 40 40"><rect x="5" y="16" width="30" height="20" fill="#fff"/><rect x="3" y="10" width="34" height="7" fill="#fff"/><rect x="18" y="10" width="4" height="26" fill="#3e74a5"/></svg>
    <strong>1000</strong><span>Project Completed</span>
  </div>
  <div class="stat" style="left:897px">
    <svg width="40" height="40" viewBox="0 0 40 40"><path d="M8 4h24l-6 14h-12z" fill="#fff"/><circle cx="20" cy="27" r="10" fill="#fff"/></svg>
    <strong>352</strong><span>Award Win</span>
  </div>
</section>

<section class="section blog">
  <h2 class="section-title" style="top:62px">Latest <b>Blog</b></h2>
  <div class="post" style="left:79px">
    <div class="photo" role="img" aria-label="Family sitting on grass in a park" style="background:linear-gradient(180deg,#8aa05a,#c8c2a0 50%,#5d7a36)"></div>
    <h3>Lorem Ipsum dummy printing and typesetting industry.</h3>
    <p>Lorem Ipsum is simply dummy text of the printing and typesetting industry. Lorem Ipsum has been the industry's standard dummy text</p>
    <div class="meta"><span><svg width="14" height="14" viewBox="0 0 14 14"><rect x="1" y="2" width="12" height="11" fill="none" stroke="#fff"/><path d="M1 5h12" stroke="#fff"/></svg>4 Nov 2017</span><span><svg width="14" height="12" viewBox="0 0 14 12"><path d="M1 1h12v8H5l-3 2V9H1z" fill="none" stroke="#fff"/></svg>Comment</span><svg class="arrow" width="24" height="20" viewBox="0 0 24 20"><path d="M2 10h18M13 3l7 7-7 7" fill="none" stroke="#fff" stroke-width="3"/></svg></div>
  </div>
  <div class="post" style="left:434px">
    <div class="photo" role="img" aria-label="Tall office towers seen from below" style="background:linear-gradient(180deg,#c9d6e2,#8a8c90 50%,#5a4a3a)"></div>
    <h3>Lorem Ipsum dummy printing and typesetting industry.</h3>
    <p>Lorem Ipsum is simply dummy text of the printing and typesetting industry. Lorem Ipsum has been the industry's standard dummy text</p>
    <div class="meta"><span><svg width="14" height="14" viewBox="0 0 14 14"><rect x="1" y="2" width="12" height="11" fill="none" stroke="#fff"/><path d="M1 5h12" stroke="#fff"/></svg>4 Nov 2017</span><span><svg width="14" height="12" viewBox="0 0 14 12"><path d="M1 1h12v8H5l-3 2V9H1z" fill="none" stroke="#fff"/></svg>Comment</span><svg class="arrow" width="24" height="20" viewBox="0 0 24 20"><path d="M2 10h18M13 3l7 7-7 7" fill="none" stroke="#fff" stroke-width="3"/></svg></div>
  </div>
  <div class="post" style="left:789px">
    <div class="photo" role="img" aria-label="People jumping against a blue sky" style="background:linear-gradient(180deg,#5f9fd6,#a8cce8 55%,#d8c890)"></div>
    <h3>Lorem Ipsum dummy printing and typesetting industry.</h3>
    <p>Lorem Ipsum is simply dummy text of the printing and typesetting industry. Lorem Ipsum has been the industry's standard dummy text</p>
    <div class="meta"><span><svg width="14" height="14" viewBox="0 0 14 14"><rect x="1" y="2" width="12" height="11" fill="none" stroke="#fff"/><path d="M1 5h12" stroke="#fff"/></svg>4 Nov 2017</span><span><svg width="14" height="12" viewBox="0 0 14 12"><path d="M1 1h12v8H5l-3 2V9H1z" fill="none" stroke="#fff"/></svg>Comment</span><svg class="arrow" width="24" height="20" viewBox="0 0 24 20"><path d="M2 10h18M13 3l7 7-7 7" fill="none" stroke="#fff" stroke-width="3"/></svg></div>
  </div>
</section>

<section class="section cta">
  <p>Are you looking for house or build residental house and light commercial...?</p>
  <div class="btn">Register Now</div>
</section>

<footer class="section footer">
  <div class="col brand-foot">
    <div style="display:flex;align-items:center;gap:10px"><span style="width:42px;height:42px;border-radius:50%;background:var(--blue);display:block"></span><span style="font-family:Lato,Arial,sans-serif;font-weight:700;font-size:25px;letter-spacing:3px;color:#fff;line-height:1">KESTREL<br>HOMES</span></div>
    <p style="margin-top:18px;width:240px;line-height:20px">Lorem Ipsum is simply dummy text of the printing.</p>
    <div class="circles"><span></span><span></span><span></span></div>
  </div>
  <div class="col" style="left:406px">
    <h4>Useful Links</h4>
    <ul class="links"><li>&bull; Home</li><li>&bull; About</li><li>&bull; Services</li><li>&bull; Projects</li><li>&bull; News</li><li>&bull; Contact</li></ul>
  </div>
  <div class="col" style="left:612px">
    <h4>Get In Touch</h4>
    <div class="contact-row"><svg width="14" height="18" viewBox="0 0 14 18"><path d="M7 17S1 10 1 6a6 6 0 0 1 12 0c0 4-6 11-6 11z" fill="none" stroke="#d6dde6" stroke-width="1.5"/><circle cx="7" cy="6" r="2" fill="#d6dde6"/></svg><div>KESTREL HOMES<br>101 - Lorem ipsum is simple<br>dummy text of print &amp; type<br>setting industry.</div></div>
    <div class="contact-row"><svg width="14" height="14" viewBox="0 0 14 14"><path d="M3 1l3 3-2 2c1 2 2 3 4 4l2-2 3 3-2 2C6 13 1 8 1 3z" fill="#d6dde6"/></svg>555-218-4460</div>
    <div class="contact-row"><svg width="16" height="12" viewBox="0 0 16 12"><rect x="0.5" y="0.5" width="15" height="11" fill="none" stroke="#d6dde6"/><path d="M1 1l7 6 7-6" fill="none" stroke="#d6dde6"/></svg>info@kestrelhomes.com</div>
  </div>
  <div class="col" style="left:876px;width:250px">
    <h4>Newsletter</h4>
    <p style="line-height:20px">Would you like to receive exclusive access to articles, white papers and our regular monthly newsletter?</p>
    <div class="email">Enter Email Id</div>
    <div class="submit">SUBMIT</div>
  </div>
</footer>

<div class="section copyright">&copy; KESTREL HOME - 2017. All Rights Reserved.</div>

</body>
</html>
```